依頼詳細
完成見学会にて使用する【のぼり旗】のデザインを募集いたします。
600x1800のサイズで【月々5万円台から(~でも可)】【ZEH】【注文住宅専門店】の3つを分かりやすく目に入りやすいデザインで作成をお願いします。
それぞれのキーワードの前後に言葉を付け加えても、無くても結構です。
(例)月々5万円台からの注文住宅!、月々5万円台からのマイホーム!
高性能 ZEH!、省エネ×創エネ ZEH!
手が届く注文住宅!など

色合いとフォントは弊社のロゴマークに合うようにお願いします。
文字の配置や大きさ等は、添付データに沿ったデザインではなくて結構です。
記載項目
キャッチフレーズ、注文住宅専門店、ロゴマーク、そよみねホーム記載の検索窓イメージ

サイズ→600x1800
希望イメージ
シンプル 複雑
単色 カラフル
暗い 明るい
日常 高級
遊び心 厳粛
未来的 伝統的
女性的 男性的
希望する色
黄・オレンジ系、緑系、茶系、添付ロゴに沿った色合い
納品ファイル
• 高解像度JPG (.jpg)
• イラストレーター形式 (.ai)
• フォトショップ形式 (.psd)
• PNG形式 (.png)
補足説明
のぼり旗で使用するロゴデータを追記しました。
よろしくお願いします。
■ 選んだ理由

掲載して欲しいキーワードが分かりやすかったため選びました。
配色も社内で評判が良く、文字も見やすかったです。

■ 提案者全員のお礼・コメント

沢山のステキなご提案をありがとうございました。
また機会がありましたら宜しくお願いいたします。

```html
<!DOCTYPE html>
<html lang="ja">
<head>
<meta charset="utf-8">
<title>完成見学会 のぼり旗 | そよみねホーム</title>
<link rel="stylesheet" href="https://fonts.googleapis.com/css2?family=M+PLUS+Rounded+1c:wght@500;800;900&display=swap">
<style>
:root{
  --red:#f01e1e;
  --white:#ffffff;
  --ink:#1a1a1a;
  --brand:#7a5a2a;
  --btn:#2b2b2b;
}
*{margin:0;padding:0;box-sizing:border-box}
html,body{width:1200px;height:3412px;overflow:hidden;background:var(--white)}
body{font-family:"M PLUS Rounded 1c",sans-serif;color:var(--ink)}
.banner{position:relative;width:1200px;height:3412px}
.head{position:absolute;left:0;top:0;width:1200px;height:832px;background:var(--red);color:var(--white);text-align:center}
.head .lead{position:absolute;top:26px;left:0;right:0;font-size:44px;font-weight:800}
.head .title{position:absolute;top:176px;left:0;right:0;font-size:176px;font-weight:900;line-height:1}
.head .spec{position:absolute;top:478px;left:0;right:0;font-size:172px;font-weight:900;line-height:1}
.head .sub{position:absolute;top:712px;left:0;right:0;font-size:52px;font-weight:800;color:var(--ink)}
.shot{position:absolute;left:0;width:1200px;height:720px;background:var(--white)}
.shot.one{top:832px}
.shot.two{top:1560px}
.shot .pic{position:absolute;left:0;top:0;width:100%;height:100%}
.shot.one .pic{background:linear-gradient(180deg,#ffffff 0%,#f2f2f2 45%,#9a9a9a 60%,#d8d8d8 80%,#6a8a4a 100%)}
.shot.two .pic{background:linear-gradient(180deg,#f4f4f4 0%,#e2e2e2 35%,#3a3a3a 50%,#d0d0d0 65%,#ffffff 100%)}
.shot .label{position:absolute;top:20px;left:0;right:0;text-align:center;font-size:56px;font-weight:800;color:var(--ink)}
.shot .tag{position:absolute;top:68px;right:150px;font-size:56px;font-weight:900;color:var(--red)}
.catch{position:absolute;left:0;top:2280px;width:1200px;height:480px;background:var(--red);color:var(--white);text-align:center;font-weight:900;font-size:140px;line-height:1}
.catch .l1{position:absolute;top:66px;left:0;right:0}
.catch .l2{position:absolute;top:262px;left:0;right:0}
.foot{position:absolute;left:0;top:2760px;width:1200px;height:652px;background:var(--white)}
.brand{position:absolute;top:130px;left:0;right:0;display:flex;justify-content:center;align-items:center;gap:28px}
.brand .mark{width:96px;height:96px;background:var(--brand)}
.brand .name{font-size:104px;font-weight:900;color:var(--brand)}
.search{position:absolute;top:336px;left:50px;width:1100px;height:120px;display:flex;align-items:center}
.search .field{width:790px;height:112px;border:6px solid var(--ink);border-radius:14px;display:flex;align-items:center;padding-left:40px;font-size:76px;font-weight:500}
.search .btn{margin-left:28px;width:200px;height:112px;background:var(--btn);border-radius:16px;color:var(--white);font-size:52px;font-weight:800;display:flex;align-items:center;justify-content:center}
.search .cursor{position:absolute;left:990px;top:62px}
</style>
</head>
<body>
<div class="banner">
  <section class="head">
    <p class="lead">月々５万円台から手が届く注文住宅！</p>
    <h1 class="title">完成見学会</h1>
    <p class="spec">ZEH 高性能</p>
    <p class="sub">省エネ×創エネ</p>
  </section>

  <section class="shot one">
    <div class="pic" role="img" aria-label="ZEH住宅の外観写真またはパース"></div>
    <p class="label">※写真orパース①</p>
    <p class="tag">ZEH</p>
  </section>

  <section class="shot two">
    <div class="pic" role="img" aria-label="ZEH住宅の室内写真またはパース"></div>
    <p class="label">※写真orパース②</p>
    <p class="tag">ZEH</p>
  </section>

  <section class="catch">
    <p class="l1">ワンランク上</p>
    <p class="l2">の注文住宅</p>
  </section>

  <section class="foot">
    <div class="brand">
      <span class="mark"></span>
      <span class="name">そよみねホーム</span>
    </div>
    <div class="search">
      <div class="field">そよみねホーム</div>
      <div class="btn">検索</div>
      <svg class="cursor" width="110" height="130" viewBox="0 0 110 130" aria-hidden="true">
        <path d="M10 10 L10 100 L34 78 L52 120 L70 112 L52 72 L86 72 Z" fill="#1a1a1a" stroke="#ffffff" stroke-width="6" stroke-linejoin="round"/>
      </svg>
    </div>
  </section>
</div>
</body>
</html>
```